Engineering firm Hero image for new web page

We are building a new webpage and need a Hero image. I have included a screen grab of the landing page showing where the image will be located. The company tag line (Engineering Tomorrow’s Automation) will be overlaid on the image so we need to be sure it works with the overlay.
We service a number of different industries, and we want something that is not overly specific so that if potential customers see something they don't recognize that we don't run them off. I have found several examples of a style that I think will work very well for us.
I want the Hero image to incorporate our competencies: Engineering, Automation, Integration, Robotics, Controls, Optimization.
There will be a follow on project to create a second image in the same theme which will highlight our industries served. Those will be: Food processing, Oil & Gas, Automotive, Aerospace, Medical, Contract Manufacturing. This image will be just below the hero and will be part of the “who we are section”

```html
<!DOCTYPE html>
<html lang="en">
<head>
<meta charset="UTF-8">
<title>Engineering Tomorrow’s Automation</title>
<link rel="stylesheet" href="https://fonts.googleapis.com/css2?family=Poppins:wght@500;600;700&display=swap">
<style>
  :root {
    --frame-blue: #8cc0ee;
    --panel-dark: #020d16;
    --brand-red: #d8232a;
    --hex-fill: #dce9f6;
    --hex-edge: #0e1b27;
    --text-white: #ffffff;
    --label-dark: #1a1a1a;
  }
  * { margin: 0; padding: 0; box-sizing: border-box; }
  html, body {
    width: 1200px; height: 667px; overflow: hidden;
    background: var(--frame-blue);
    font-family: 'Poppins', sans-serif;
  }
  .hero-canvas { position: relative; width: 1200px; height: 667px; }
  .hero-panel {
    position: absolute; left: 79px; top: 44px;
    width: 1042px; height: 578px;
    background: var(--panel-dark);
    overflow: hidden;
  }
  .competency-graphic { position: absolute; left: 0; top: 0; width: 1042px; height: 578px; }
  .tagline {
    position: absolute; left: 61px; top: 142px;
    color: var(--text-white);
    font-weight: 700; font-size: 57px; line-height: 65px;
    letter-spacing: -1px;
  }
  .cta-button {
    position: absolute; left: 67px; top: 378px;
    width: 190px; height: 53px;
    background: var(--brand-red); color: var(--text-white);
    border-radius: 4px;
    font-weight: 600; font-size: 22px;
    display: flex; align-items: center; justify-content: center;
    text-decoration: none;
  }
  .hex-shape { fill: var(--hex-fill); stroke: var(--hex-edge); stroke-width: 7; }
  .hex-icon { fill: none; stroke: var(--brand-red); stroke-width: 3.5; stroke-linecap: round; stroke-linejoin: round; }
  .hex-label { font-family: 'Poppins', sans-serif; font-weight: 500; font-size: 16px; fill: var(--label-dark); text-anchor: middle; }
  .edge-word { font-family: 'Poppins', sans-serif; font-weight: 500; font-size: 15px; fill: #2a2f36; }
</style>
</head>
<body>
<div class="hero-canvas">
  <section class="hero-panel">
    <svg class="competency-graphic" viewBox="95 53 1250 694" xmlns="http://www.w3.org/2000/svg">
      <defs>
        <radialGradient id="core-glow" cx="50%" cy="50%" r="50%">
          <stop offset="0" stop-color="#ffd9b8"/>
          <stop offset="0.25" stop-color="#f07a38"/>
          <stop offset="0.55" stop-color="#7a2c12"/>
          <stop offset="1" stop-color="#020d16" stop-opacity="0"/>
        </radialGradient>
        <polygon id="hex" points="0,-88 88,-44 88,44 0,88 -88,44 -88,-44"/>
      </defs>

      <circle role="img" aria-label="Glowing gear touched by a fingertip" cx="1000" cy="420" r="330" fill="url(#core-glow)"/>

      <text class="edge-word" x="1252" y="264">Food</text>

      <g transform="translate(833,220)">
        <use href="#hex" class="hex-shape"/>
        <g class="hex-icon">
          <circle cx="-14" cy="-26" r="26"/><circle cx="-14" cy="-26" r="11"/>
          <path d="M-2 -42 H24 M0 -32 H30 M2 -20 H30 M-2 -10 H24"/>
          <circle cx="28" cy="-42" r="3"/><circle cx="34" cy="-32" r="3"/><circle cx="34" cy="-20" r="3"/><circle cx="28" cy="-10" r="3"/>
        </g>
      </g>

      <g transform="translate(745,378)">
        <use href="#hex" class="hex-shape"/>
        <g class="hex-icon">
          <circle cx="14" cy="-42" r="14"/><circle cx="14" cy="-42" r="5"/>
          <path d="M-30 -48 H-10 L0 -42 M-22 -26 H-8"/>
          <path d="M-46 4 H-30 L-8 -10 H30 M-46 4 V22 H-28"/>
        </g>
      </g>

      <g transform="translate(833,555)">
        <use href="#hex" class="hex-shape"/>
        <g class="hex-icon">
          <circle cx="-22" cy="-46" r="18"/>
          <path d="M-8 -42 A22 22 0 0 1 36 -42 Z"/>
          <circle cx="14" cy="-26" r="14"/>
          <path d="M-20 22 V6 A34 20 0 0 1 48 6 V22"/>
        </g>
      </g>

      <g transform="translate(1160,225)">
        <use href="#hex" class="hex-shape"/>
        <g class="hex-icon">
          <path d="M-50 24 H8 M-40 24 V16 H-4 V24"/>
          <path d="M-22 16 L-28 -26 L10 -50 L34 -26"/>
          <circle cx="-28" cy="-26" r="6"/><circle cx="10" cy="-50" r="6"/>
          <path d="M26 -20 L30 -4 M42 -20 L38 -4"/>
        </g>
      </g>

      <g transform="translate(1248,378)">
        <use href="#hex" class="hex-shape"/>
        <g class="hex-icon">
          <rect x="-22" y="-62" width="44" height="82" rx="20"/>
          <path d="M0 -48 V-40 M-12 -16 V-6 M0 -16 V-6 M12 -16 V-6"/>
          <circle cx="0" cy="8" r="2"/>
        </g>
      </g>

      <g transform="translate(1160,540)">
        <use href="#hex" class="hex-shape"/>
        <g class="hex-icon">
          <circle cx="0" cy="-18" r="34" stroke-dasharray="10 6"/>
          <circle cx="0" cy="-18" r="24"/>
          <path d="M-12 -8 L-2 -20 L4 -14 L14 -28 M8 -28 H14 V-22"/>
        </g>
      </g>

      <g class="hex-labels">
        <text class="hex-label" x="833" y="272">Integration</text>
        <text class="hex-label" x="745" y="430">Automation</text>
        <text class="hex-label" x="833" y="607">Engineering</text>
        <text class="hex-label" x="1160" y="277">Robotics</text>
        <text class="hex-label" x="1248" y="430">Controls</text>
        <text class="hex-label" x="1160" y="592">Optimization</text>
      </g>
    </svg>

    <h1 class="tagline">Engineering<br>Tomorrow’s<br>Automation</h1>
    <a class="cta-button" href="#">Learn More</a>
  </section>
</div>
</body>
</html>
```